Cutting Board Oil Label

I would like a label created for our custom made cutting board oil. The bottle will be clear and come in several different sizes. I have included the current label we use. We would like the information to stay the same, but more aesthetically pleasing and professionally presented. I am also including our logo and the current label of our biggest competitor.

```html
<!DOCTYPE html>
<html lang="en">
<head>
<meta charset="utf-8">
<title>Cutting Board Conditioner Label</title>
<link href="https://fonts.googleapis.com/css2?family=Baloo+2:wght@600;700&family=Roboto:wght@400;500;700&family=Roboto+Slab:wght@400&display=swap" rel="stylesheet">
<style>
  :root {
    --teal: #23bcc1;
    --slate: #5f6367;
    --ink: #616468;
    --sun: #e9c98c;
    --white: #ffffff;
    --paper: #ffffff;
  }
  * { box-sizing: border-box; margin: 0; padding: 0; }
  html, body { width: 859px; height: 1200px; overflow: hidden; background: var(--paper); }
  .sheet {
    width: 859px; height: 1200px;
    display: flex; justify-content: space-between; align-items: flex-start;
    padding: 250px 48px 0;
    font-family: "Roboto", Arial, sans-serif;
  }
  .label { width: 366px; display: flex; flex-direction: column; align-items: center; }

  .brand { display: flex; align-items: center; gap: 10px; margin-bottom: 10px; }
  .brand-dot { width: 22px; height: 22px; border-radius: 50%; background: var(--sun); }
  .brand-name { font-family: "Roboto", Arial, sans-serif; font-weight: 500; font-size: 30px; color: var(--ink); letter-spacing: 0.5px; }
  .tagline {
    font-family: "Roboto Slab", Georgia, serif; font-size: 12px; color: var(--teal);
    letter-spacing: 0.2px; margin-bottom: 14px; white-space: nowrap;
  }

  .front-panel { width: 100%; background: var(--teal); border-radius: 14px 14px 0 0; overflow: hidden; text-align: center; }
  .product-title { font-family: "Baloo 2", "Trebuchet MS", sans-serif; color: var(--white); line-height: 0.8; padding-top: 22px; }
  .product-title .line-cutting { display: block; font-size: 76px; font-weight: 700; padding-left: 20px; }
  .product-title .line-board { display: block; font-size: 82px; font-weight: 700; text-align: left; padding-left: 56px; margin-top: 6px; }
  .product-title .line-type { display: block; font-size: 30px; font-weight: 600; margin-top: 2px; padding-left: 40px; }
  .uses { color: var(--white); font-weight: 500; font-size: 13px; line-height: 1.3; margin-top: 28px; }
  .claims { color: var(--white); font-weight: 500; font-size: 19px; letter-spacing: 0.6px; margin-top: 24px; }
  .made-with { color: var(--white); font-size: 9.5px; margin-top: 2px; }
  .ingredients { color: var(--white); font-size: 10px; margin-top: 2px; padding-bottom: 20px; }
  .footer-band {
    background: var(--slate); color: var(--white); font-weight: 500; font-size: 10.5px;
    display: flex; justify-content: center; gap: 16px; padding: 15px 0 16px;
  }

  .back-panel { width: 100%; background: var(--teal); border-radius: 14px; padding: 22px 12px 26px 14px; }
  .directions { color: var(--white); font-size: 10.4px; line-height: 1.32; text-align: justify; }
</style>
</head>
<body>
<main class="sheet">
  <section class="label label--front">
    <div class="brand"><span class="brand-dot"></span><span class="brand-name">Laurel Creek Goods</span></div>
    <p class="tagline">HANDCRAFTED GOODS for EVERYDAY KITCHENS</p>
    <div class="front-panel">
      <h1 class="product-title">
        <span class="line-cutting">Cutting</span>
        <span class="line-board">Board</span>
        <span class="line-type">Conditioner</span>
      </h1>
      <p class="uses">For use on cutting boards, butcher blocks,<br>wood utensils, and any other wood products.</p>
      <p class="claims">FOOD SAFE &nbsp;-&nbsp; ALL NATURAL</p>
      <p class="made-with">Made with:</p>
      <p class="ingredients">Beeswax, Mineral Oil,Orange Oil, Lemon Oil, and Vitamin E</p>
      <div class="footer-band"><span>Made in the USA</span><span>www.LaurelCreekGoods.com</span></div>
    </div>
  </section>

  <section class="label label--back">
    <div class="brand"><span class="brand-dot"></span><span class="brand-name">Laurel Creek Goods</span></div>
    <p class="tagline">HANDCRAFTED GOODS for EVERYDAY KITCHENS</p>
    <div class="back-panel">
      <p class="directions">Directions: Apply a generous amount of conditioner with a clean, lint free cloth. For best results, allow board to soak in conditioner overnight. Using a clean, lint free cloth, buff and remove any excess conditioner. For new or unconditioned cutting boards, butcher blocks, or wooden kitchen utensils we recommend repeating the process a second time to ensure your wood is properly sealed. Recondition about once a month (depending on frequency of use) or when the board begins to become dry to the touch.</p>
    </div>
  </section>
</main>
</body>
</html>
```